Business cards for a high-end menswear store

I would like to come up with a design for our business cards.
Two different ones: one for general sales and one for the owner. It is a high-end menswear store.

Our address is: 4817 Morneau Boulevard, Montreal, QC, K7P4M2
phone number: 514-286-5937
insta: MAISONVERLAINE
Website: www.maisonverlaine.example
email (general card): info@maisonverlaine.example
email (owner): bastien@maisonverlaine.example

I have attached our logo in an ai and eps file format. You can see our old cards as well. I am looking for a modern and clean look.

Target Market(s)

High-End Clothing Market

Industry/Entity Type

Retail, Clothing, Luxury Clothing

Contact Information for Business Card

Address, Name, Email, Website, Social Info,

Font styles to use
Serif

Colors

Designer to choose colors to be used in the design.

Requirements
Must have
• Address, Name, Email, Website, Social Info,
Nice to have
• QR Code that brings you to the website

```html
<!DOCTYPE html>
<html lang="en">
<head>
<meta charset="utf-8">
<title>Maison Verlaine – Business Cards</title>
<link rel="stylesheet" href="https://fonts.googleapis.com/css2?family=Tinos:wght@400;700&display=swap">
<style>
  :root {
    --ink: #000000;
    --paper: #ffffff;
    --backdrop: #a6a6a6;
  }
  * { margin: 0; padding: 0; box-sizing: border-box; }
  html, body { width: 1200px; height: 1198px; overflow: hidden; }
  body {
    position: relative;
    background: var(--backdrop);
    font-family: "Tinos", "Times New Roman", serif;
  }
  .card { position: absolute; left: 312px; width: 604px; height: 345px; }
  .card--front { top: 224px; background: var(--ink); color: var(--paper); }
  .card--back { top: 638px; background: var(--paper); color: var(--ink); }

  .brand-lockup {
    position: absolute; left: 0; right: 0; top: 360px - 224px;
    display: flex; flex-direction: column; align-items: center; gap: 14px;
  }
  .card--front .brand-lockup { top: 110px; }
  .brand-square { width: 56px; height: 56px; background: var(--paper); }
  .brand-name { font-size: 24px; letter-spacing: 4px; }
  .tagline {
    position: absolute; left: 0; right: 0; top: 228px;
    text-align: center; font-size: 22px; letter-spacing: 0.3px;
  }

  .holder-name {
    position: absolute; left: 62px; top: 48px;
    font-size: 30px; font-weight: 700; letter-spacing: 0.5px;
  }
  .holder-role { position: absolute; left: 62px; top: 84px; font-size: 19px; }
  .divider { position: absolute; left: 61px; top: 132px; width: 304px; height: 2px; background: var(--ink); }
  .contact-list { position: absolute; left: 61px; top: 144px; list-style: none; }
  .contact-list li {
    display: flex; align-items: center; height: 26px; font-size: 16px;
  }
  .contact-list svg { width: 15px; height: 15px; margin-right: 17px; fill: var(--ink); }

  .back-brand {
    position: absolute; left: 462px; top: 140px; width: 120px;
    display: flex; flex-direction: column; align-items: center; gap: 10px;
  }
  .back-brand .brand-square { width: 64px; height: 64px; background: var(--ink); }
  .back-brand .brand-name { font-size: 16px; letter-spacing: 2px; text-align: center; line-height: 1.2; }

  .address-band {
    position: absolute; left: 0; top: 267px; width: 100%; height: 40px;
    background: var(--ink); color: var(--paper);
    display: flex; align-items: center; padding-left: 62px; font-size: 19px;
  }
  .address-band svg { width: 16px; height: 22px; margin-right: 16px; fill: var(--paper); }
</style>
</head>
<body>

<section class="card card--front" aria-label="Card front">
  <div class="brand-lockup">
    <span class="brand-square"></span>
    <span class="brand-name">MAISON VERLAINE</span>
  </div>
  <p class="tagline">HIGH-END MENSWEAR STORE</p>
</section>

<section class="card card--back" aria-label="Card back">
  <h1 class="holder-name">BASTIEN LAROCHE</h1>
  <p class="holder-role">Owner</p>
  <div class="divider"></div>
  <ul class="contact-list">
    <li>
      <svg viewBox="0 0 24 24" aria-hidden="true"><path d="M6.6 10.8a15.1 15.1 0 0 0 6.6 6.6l2.2-2.2c.3-.3.7-.4 1-.2 1.1.4 2.3.6 3.6.6.6 0 1 .4 1 1V20c0 .6-.4 1-1 1A17 17 0 0 1 3 4c0-.6.4-1 1-1h3.5c.6 0 1 .4 1 1 0 1.3.2 2.5.6 3.6.1.3 0 .7-.2 1z"/></svg>
      514-286-5937
    </li>
    <li>
      <svg viewBox="0 0 24 24" aria-hidden="true"><path d="M2 5h20v14H2z M3.5 6.5 12 12l8.5-5.5" fill="none" stroke="#000" stroke-width="0"/><path d="M2 5h20v2l-10 6L2 7z M2 9l10 6 10-6v10H2z"/></svg>
      bastien@maisonverlaine.example
    </li>
    <li>
      <svg viewBox="0 0 24 24" aria-hidden="true"><circle cx="12" cy="12" r="9.5" fill="none" stroke="#000" stroke-width="2"/><ellipse cx="12" cy="12" rx="4" ry="9.5" fill="none" stroke="#000" stroke-width="2"/><path d="M2.5 12h19" stroke="#000" stroke-width="2"/></svg>
      www.maisonverlaine.example
    </li>
    <li>
      <svg viewBox="0 0 24 24" aria-hidden="true"><rect x="3" y="3" width="18" height="18" rx="5" fill="none" stroke="#000" stroke-width="2"/><circle cx="12" cy="12" r="4" fill="none" stroke="#000" stroke-width="2"/></svg>
      MAISONVERLAINE
    </li>
  </ul>

  <div class="back-brand">
    <span class="brand-square"></span>
    <span class="brand-name">MAISON<br>VERLAINE</span>
  </div>

  <div class="address-band">
    <svg viewBox="0 0 16 22" aria-hidden="true"><path d="M8 0a8 8 0 0 0-8 8c0 6 8 14 8 14s8-8 8-14a8 8 0 0 0-8-8zm0 11a3 3 0 1 1 0-6 3 3 0 0 1 0 6z"/></svg>
    4817 Morneau Boulevard, Montreal, QC, K7P4M2
  </div>
</section>

</body>
</html>
```